Redesign start page for existing online shop

We are selling building material (chimneys and flue pipes) as well as fireplaces (stoves). For this online shop we need a new start page. The domain is brunnfeld-bauwaren.de. Here you can see the current design. We want a smoother design with just one banner in the middle instead of the three in the first row. The look has to be more professional and trustworthy. You can therefore play with the colors. We want to try some different orange instead of our yellow / orange color. A few more things: - The phone number has to be bigger and more highlighted - So the 5 advantages at the top should be shown in a different way - New design for the products below - New footer

Target Market(s)

Germany and other countries in Europe.

Industry/Entity Type

Home Builder

Number of Pages Required

1 page

Other font styles liked:
• Please se the font on our current site.

Colors
f78f20
f68d4c

Requirements
Must have
• - Clear design - Trustworthy look - All elements Which are now shown shoulderstand be still there after redesigning -
Nice to have
• - See the Following sites to have a clou about our wishes: kalvesto.de flinkrabe.de

```html
<!DOCTYPE html>
<html lang="de">
<head>
<meta charset="utf-8">
<title>Brunnfeld Bauwaren – Schornsteine und Zubehör</title>
<link href="https://fonts.googleapis.com/css2?family=Open+Sans:wght@400;600;700;800&display=swap" rel="stylesheet">
<style>
:root{
  --orange:#f78f20;
  --orange-soft:#f68d4c;
  --red:#ef4f1f;
  --ink:#333;
  --muted:#666;
  --line:#e2e2e2;
  --grey-bg:#efefef;
  --dark:#3b3b3b;
  --white:#fff;
}
*{box-sizing:border-box;margin:0;padding:0}
html,body{width:1200px;height:3758px;overflow:hidden}
body{font-family:"Open Sans",Arial,sans-serif;color:var(--ink);background:var(--white);font-size:13px}
.wrap{width:1050px;margin:0 auto;position:relative}
a{color:inherit;text-decoration:none}

/* top bar */
.topbar{height:26px;background:#f6f6f6;border-bottom:1px solid var(--line);font-size:11px;color:var(--muted)}
.topbar .wrap{display:flex;justify-content:space-between;align-items:center;height:26px}
.topbar .left span{margin-right:22px}
.topbar .right{display:flex;gap:18px;align-items:center}
.stars{color:var(--orange);letter-spacing:1px}

/* header */
.header{height:100px}
.header .wrap{display:flex;align-items:center;height:100px}
.brand{display:flex;align-items:center;gap:12px;width:400px}
.brand-dot{width:48px;height:48px;border-radius:50%;background:var(--orange)}
.brand-name{font-weight:800;font-size:22px;line-height:24px;color:#555;letter-spacing:.5px}
.search{display:flex;align-items:center;width:300px;height:36px;background:#dcdcdc;border-radius:18px;padding-left:16px;font-size:11px;color:#888;position:relative}
.search .go{position:absolute;right:-6px;width:40px;height:40px;border-radius:50%;background:var(--orange);display:flex;align-items:center;justify-content:center}
.phone{margin-left:auto;text-align:right}
.phone .num{font-size:24px;font-weight:800;color:var(--red);display:flex;align-items:center;gap:8px}
.phone .hours{font-size:11px;color:var(--muted)}

/* nav */
.nav{height:38px;border-bottom:1px solid var(--line)}
.nav .wrap{display:flex;align-items:center;height:38px;font-weight:700;font-size:13px}
.nav .wrap span{margin-right:44px}
.rating-badge{position:absolute;right:0;top:-6px;width:64px;height:70px;background:#fff;border:1px solid var(--line);display:flex;flex-direction:column;align-items:center;justify-content:center;gap:4px;z-index:2}
.rating-badge i{display:block;width:34px;height:34px;border-radius:50%;background:#444}
.rating-badge b{font-size:9px;color:var(--orange)}
.usp{height:22px;background:var(--orange);color:#fff;font-size:11px;font-weight:700}
.usp .wrap{display:flex;gap:70px;align-items:center;height:22px;padding-left:10px}

/* hero */
.hero{height:392px;position:relative;width:1050px;margin:0 auto;background:linear-gradient(180deg,#7fb3e0 0%,#a9cdec 45%,#b46b49 62%,#8b4c34 100%)}
.hero .photo-card{position:absolute;right:35px;top:14px;width:70px;height:95px;background:linear-gradient(#3a3a3a,#6b5c4d)}
.hero h1{position:absolute;left:510px;top:120px;color:#fff;font-size:40px;line-height:48px;font-weight:800}
.btn{display:inline-flex;align-items:center;gap:8px;background:var(--red);color:#fff;font-weight:700;border-radius:3px}
.hero .btn{position:absolute;left:565px;top:240px;height:62px;padding:0 38px;font-size:20px}

/* brands */
.brands{height:66px}
.brands .wrap{display:flex;align-items:center;height:66px;gap:60px;padding-left:205px}
.brands small{font-size:11px;color:var(--muted)}
.brands .mark{font-size:22px;font-weight:800;color:#1d3f86}

/* features */
.features{padding-top:56px;height:390px}
.features .wrap{display:grid;grid-template-columns:repeat(4,1fr);gap:30px;padding:0 20px}
.feature{text-align:center}
.feature .icon{width:62px;height:62px;border:2px solid var(--orange);margin:0 auto 20px;display:flex;align-items:center;justify-content:center}
.feature h3{font-size:15px;line-height:20px;font-weight:600;margin-bottom:12px}
.feature p{font-size:10.5px;line-height:15px;color:var(--muted)}

/* how */
.how{background:var(--grey-bg);width:1050px;margin:0 auto;height:460px;text-align:center;padding-top:52px}
.how h2{font-size:34px;font-weight:800}
.how .sub{font-size:14px;margin-top:4px}
.steps{display:flex;justify-content:center;gap:70px;margin-top:40px}
.step{width:150px}
.step .circle{width:100px;height:100px;border-radius:50%;border:2px solid #bdbdbd;background:#fff;margin:0 auto 14px;display:flex;align-items:center;justify-content:center}
.step span{font-size:11px;color:var(--muted);line-height:15px;display:block}
.cta{display:flex;justify-content:center;align-items:center;gap:28px;margin-top:34px;font-weight:700;font-size:17px}
.cta .btn{height:42px;padding:0 20px;font-size:13px}

/* products */
.products{padding-top:48px;height:528px}
.products .wrap{display:grid;grid-template-columns:repeat(4,1fr);gap:20px}
.card{border:1px solid var(--line);height:432px;text-align:center}
.card .img{height:228px;position:relative;margin:8px}
.card .price{position:absolute;right:-8px;bottom:0;background:var(--red);color:#fff;font-weight:700;font-size:16px;padding:9px 14px}
.card h3{font-size:15px;font-weight:600;margin-top:22px}
.card p{font-size:10.5px;line-height:15px;color:var(--muted);margin:8px 20px 0;height:62px}
.card .more{display:inline-block;margin-top:16px;background:var(--orange);color:#fff;font-size:10px;font-weight:700;padding:9px 22px;border-radius:16px}

/* seo text */
.seo{background:var(--dark);color:#e6e6e6;height:1212px;padding-top:40px}
.seo h2{color:var(--orange);font-size:17px;line-height:24px;font-weight:700;margin-bottom:18px}
.seo h3{color:#fff;font-size:15px;font-weight:700;margin:26px 0 12px}
.seo p{font-size:12.5px;line-height:22px}
.seo .hl{color:var(--orange)}

/* trust */
.trust{height:255px;border-bottom:1px solid var(--line)}
.trust h2{text-align:center;font-size:18px;font-weight:600;padding:28px 0 36px}
.trust .wrap{display:grid;grid-template-columns:1fr 1fr;gap:40px}
.trust-box{border:1px solid var(--line);height:128px;display:flex;align-items:center;gap:22px;padding:0 22px}
.trust-box .seal{flex:none;width:82px;height:82px;border-radius:50%;background:linear-gradient(#e9c12f,#9e7d14)}
.trust-box .flag{flex:none;width:82px;height:82px;border-radius:50%;background:linear-gradient(#222 33%,#d32 33% 66%,#f2c200 66%)}
.trust-box p{font-size:11px;line-height:17px;color:var(--muted)}

/* footer */
.footer{height:130px;padding-top:24px}
.footer .wrap{display:grid;grid-template-columns:1fr 1fr 1.2fr 1.2fr 1fr;font-size:11px;line-height:19px;color:var(--muted)}
.footer strong{color:var(--ink);font-size:12px}
.footer .tel{color:var(--red);font-weight:800;font-size:17px}
.pay{height:95px;border-top:1px solid var(--line)}
.pay .wrap{display:flex;align-items:center;height:95px;gap:12px}
.pay .label{font-size:15px;font-weight:600;margin-right:12px}
.pay .card-mark{height:36px;padding:0 10px;border:1px solid var(--line);border-radius:3px;display:flex;align-items:center;font-size:11px;font-weight:700;color:#555}
.social{margin-left:auto;display:flex;gap:8px}
.social i{display:block;width:32px;height:32px;border-radius:50%;background:#bdbdbd}
</style>
</head>
<body>

<div class="topbar"><div class="wrap">
  <div class="left"><span>Sicher einkaufen ▾</span><span>Service ▾</span><span>Beratung &amp; Kontakt ▾</span></div>
  <div class="right"><span><span class="stars">★★★★★</span> Sehr gut (4.80/5.00)</span><span>Mein Konto</span><span>Warenkorb</span></div>
</div></div>

<header class="header"><div class="wrap">
  <div class="brand"><span class="brand-dot"></span><span class="brand-name">BRUNNFELD<br>BAUWAREN</span></div>
  <div class="search">Suchbegriff oder Artikelnummer
    <span class="go"><svg width="18" height="18" viewBox="0 0 18 18"><circle cx="7.5" cy="7.5" r="5.5" fill="none" stroke="#fff" stroke-width="2.2"/><path d="M11.5 11.5l5 5" stroke="#fff" stroke-width="2.4"/></svg></span>
  </div>
  <div class="phone">
    <div class="num"><svg width="20" height="20" viewBox="0 0 24 24"><path fill="#ef4f1f" d="M6.6 10.8a15.1 15.1 0 006.6 6.6l2.2-2.2c.3-.3.7-.4 1-.2 1.1.4 2.3.6 3.6.6.6 0 1 .4 1 1V20c0 .6-.4 1-1 1A17 17 0 013 4c0-.6.4-1 1-1h3.5c.6 0 1 .4 1 1 0 1.3.2 2.5.6 3.6.1.3 0 .7-.2 1z"/></svg>0821 / 447 318 0</div>
    <div class="hours">Mo. – Fr. von 09:00 bis 18:00 Uhr</div>
  </div>
</div></header>

<nav class="nav"><div class="wrap">
  <span>Online-Shop ▾</span><span>Service ▾</span><span>Standorte</span><span>Für Händler</span><span>Installateure</span>
  <div class="rating-badge"><i></i><b>★★★★★</b></div>
</div></nav>

<div class="usp"><div class="wrap"><span>✔ Heizung inkl. Montage</span><span>✔ Festpreisangebot</span><span>✔ Kostenlos &amp; unverbindlich</span></div></div>

<section class="hero" role="img" aria-label="Foto: Ziegeldach mit gemauertem Schornstein vor blauem Himmel">
  <div class="photo-card" role="img" aria-label="Foto eines Beraters"></div>
  <h1>In 5 Minuten zum<br>Schornstein</h1>
  <a class="btn" href="#">Zum Angebot ▸</a>
</section>

<section class="brands"><div class="wrap">
  <small>Unsere Marken:</small>
  <span class="mark">Feronis</span>
  <span class="mark">Ventora</span>
  <span class="mark" style="color:#a3202a">Halmbach</span>
</div></section>

<section class="features"><div class="wrap">
  <div class="feature">
    <div class="icon"><svg width="34" height="34" viewBox="0 0 34 34" fill="none" stroke="#f78f20" stroke-width="2.5"><rect x="7" y="4" width="20" height="26"/><path d="M11 11h12M11 17h12M11 23h7"/></svg></div>
    <h3>Verbindliches<br>Heizungs-Angebot sofort!</h3>
    <p>Geben Sie nur wenige Eckdaten zu Ihrem Haus in unseren Angebotsrechner ein und Sie erhalten innerhalb weniger Stunden ein verbindliches Angebot für Ihre neue Heizung!</p>
  </div>
  <div class="feature">
    <div class="icon"><svg width="34" height="34" viewBox="0 0 34 34" fill="none" stroke="#f78f20" stroke-width="3"><path d="M6 28L20 14M20 14l4-8 4 4-8 4M6 6l22 22"/></svg></div>
    <h3>Mehr als 30 Jahre<br>Meisterqualität!</h3>
    <p>Erfahrung und Kompetenz sind der Garant für unseren hervorragenden Service. Mit rund 100 geschulten und kompetenten Heizungsfachmännern sind wir deutschlandweit für Sie im Einsatz!</p>
  </div>
  <div class="feature">
    <div class="icon"><svg width="34" height="34" viewBox="0 0 34 34" fill="none" stroke="#f78f20" stroke-width="2.5"><path d="M4 17L17 5l13 12M8 14v15h18V14"/><path d="M14 29v-8h6v8"/></svg></div>
    <h3>Neue Heizung bereits<br>ab 39 € im Monat!</h3>
    <p>Eine neue, umweltfreundliche und energiesparende Heizung liefern und installieren wir Ihnen bereits für 39,- Euro im Monat. Durch die mögliche Energieeinsparung ist Ihre neue Heizung fast „geschenkt“!</p>
  </div>
  <div class="feature">
    <div class="icon"><svg width="34" height="34" viewBox="0 0 34 34" fill="none" stroke="#f78f20" stroke-width="2.5"><circle cx="17" cy="17" r="12"/><path d="M17 10c3 4 5 6 0 14-5-8-3-10 0-14z"/></svg></div>
    <h3>10 Jahre Garantie auf<br>Ihre neue Heizung!</h3>
    <p>Wir verbauen Qualität und bieten Ihnen daher ab sofort auf alle von uns eingebauten Heizkessel eine 10-Jahres-Garantie! So müssen Sie sich keine Sorgen mehr machen, falls Ihre Anlage doch einmal ausfallen sollte!</p>
  </div>
</div></section>

<section class="how">
  <h2>So funktioniert’s</h2>
  <p class="sub">In wenigen Schritten zum richtigen Angebot  für Ihre Sanierung</p>
  <div class="steps">
    <div class="step"><div class="circle"><svg width="44" height="44" viewBox="0 0 44 44" fill="none" stroke="#555" stroke-width="2"><rect x="6" y="9" width="32" height="22" rx="2"/><path d="M2 35h40"/></svg></div><span>Daten online eingeben</span></div>
    <div class="step"><div class="circle"><svg width="44" height="44" viewBox="0 0 44 44" fill="none" stroke="#555" stroke-width="2"><path d="M5 22L22 7l17 15M10 18v19h24V18"/><rect x="18" y="26" width="8" height="11"/></svg></div><span>Aufmaß und Beratung<br>durch Kundenberater</span></div>
    <div class="step"><div class="circle"><svg width="44" height="44" viewBox="0 0 44 44" fill="none" stroke="#555" stroke-width="2"><rect x="10" y="5" width="24" height="34"/><path d="M15 14h14M15 20h14M15 26h9"/></svg></div><span>Angebot von 2 ausgewählten<br>Handwerkern</span></div>
    <div class="step"><div class="circle"><svg width="44" height="44" viewBox="0 0 44 44" fill="none" stroke="#555" stroke-width="2"><rect x="3" y="13" width="24" height="16"/><path d="M27 18h8l6 6v5H27z"/><circle cx="11" cy="32" r="4"/><circle cx="33" cy="32" r="4"/></svg></div><span>Ausführung</span></div>
  </div>
  <div class="cta">Jetzt unverbindliche eine Anfrage stellen! <a class="btn" href="#">Anfrage stellen ▸</a></div>
</section>

<section class="products"><div class="wrap">
  <article class="card">
    <div class="img" role="img" aria-label="Produktfoto: Schornsteinverlängerung aus Edelstahl" style="background:linear-gradient(90deg,#f4f4f4,#cfcfcf 50%,#f4f4f4)"><span class="price">ab € 63,00</span></div>
    <h3>Schornsteinverlängerung</h3>
    <p>Kaminverlängerungen frei konfigurierbar nach Ihren Wunschmaßen und in Handarbeit nach höchsten Ansprüchen hergestellt.</p>
    <a class="more" href="#">JETZT ANSEHEN ▸</a>
  </article>
  <article class="card">
    <div class="img" role="img" aria-label="Produktfoto: Schornsteinabdeckung aus Edelstahl" style="background:linear-gradient(180deg,#f6f6f6,#d4d4d4 60%,#f6f6f6)"><span class="price">ab € 116,50</span></div>
    <h3>Schornsteinabdeckung</h3>
    <p>Kaminabdeckungen für alle Schornsteine individuell bestellen. Höchste Langlebigkeit und Qualität für Ihren Schornstein.</p>
    <a class="more" href="#">JETZT ANSEHEN ▸</a>
  </article>
  <article class="card">
    <div class="img" role="img" aria-label="Produktfoto: Wanddurchführung mit Dämmplatten" style="background:linear-gradient(135deg,#f2f2f2,#d9d6cf 55%,#f2f2f2)"><span class="price">ab € 99,99</span></div>
    <h3>Wanddurchführung</h3>
    <p>Wanddurchführungen für die sichere Durchführung von Abgasrohren durch Hauswände. Brandschutz auf höchstem Niveau.</p>
    <a class="more" href="#">JETZT ANSEHEN ▸</a>
  </article>
  <article class="card">
    <div class="img" role="img" aria-label="Produktfoto: schwarzes Ofenrohr mit Bogen" style="background:linear-gradient(90deg,#f4f4f4,#3a3a3a 45%,#2a2a2a 60%,#f4f4f4)"><span class="price">ab € 9,90</span></div>
    <h3>Ofenrohr</h3>
    <p>Ofenrohre in den Farben schwarz oder gussgrau in Premiumqualität direkt hier bestellen. Höchste Qualität für Ihre Sicherheit.</p>
    <a class="more" href="#">JETZT ANSEHEN ▸</a>
  </article>
</div></section>

<section class="seo"><div class="wrap">
  <h2>Edelstahlschornsteine, Schornsteinverlängerungen, Ofenrohre und Schornstein Zubehör – alles bei brunnfeld-bauwaren.de<br>günstig kaufen.</h2>
  <p>Kann ich einen Edelstahlschornstein im Internet kaufen? Diese Frage haben Sie sich bestimmt noch nie gestellt. Bei anderen Waren ist das eine Selbstverständlichkeit, aber bei einem Edelstahlkamin denkt man zunächst nicht ans Onlineshopping. Dabei gibt es schon seit einigen Jahren diverse Plattformen, die alles rund um das Thema Edelstahlschornstein anbieten. Allerdings betreiben diese Anbieter ihre Webshops nur nebenher. Dies spiegelt sich in der schlechten Benutzerfreundlichkeit und der teilweise stark veralteten Technik der Seiten wieder. Brunnfeld Bauwaren hat daher einen neuen Weg gewählt: Das Ziel war es, einen Onlineshop für Edelstahlschornsteine und Schornstein Zubehör auf die Beine zu stellen, der nicht nur professionell und nach dem neuesten Stand der Technik aufgebaut ist, sondern Ihnen auch die Sicherheit und Usability bietet, die Sie von großen Onlineplattformen gewohnt sind. Mit einer effizienten Organisation, moderner Technik und jahrelanger Erfahrung mit dem Produkt Edelstahlschornstein konnte dieser Anspruch erfüllt werden. Beste Usability, geprüfter Datenschutz, hochwertige Waren und eine kompetente telefonische Beratung runden Ihr Einkaufserlebnis bei brunnfeld-bauwaren.de ab.</p>

  <h3>Edelstahlschornstein, Schornstein Bausatz und Edelstahlkamin – alles aus einer Hand.</h3>
  <p>Ob Sie einen doppelwandigen Edelstahlschornstein, eine Schornsteinsanierung für Ihren alten gemauerten Kamin oder einen Schornstein Bausatz für Ihr Haus suchen: hier werden Sie fündig. Bei brunnfeld-bauwaren finden Sie eine große Auswahl an in Deutschland hergestellten Edelstahlschornsteinen des Herstellers Feronis. Diese Schornsteine werden nach modernsten Produktionsmethoden aus hochwertigem V4A Edelstahl hergestellt und unterliegen strengsten Qualitätsvorschriften. Die Feronis GmbH gewährt Ihnen darüber hinaus auch eine Garantie von 25 Jahren auf jeden in diesem Onlineshop erworbenen Edelstahlschornstein. Ganz einfach: Sicherheit zum besten Preis!</p>
  <p style="margin-top:14px">Und noch ein Tipp: Alle Schornsteine lassen sich wunderbar mit einem <span class="hl">Ofenrohr</span> von Feronis anschließen. Hier gibt es eine große Auswahl an verschiedenen Längen, Farben und Winkeln. Außerdem sind seit Kurzem auch isolierte Ofenrohre lieferbar. Diese doppelwandigen Ofenrohre verringern den Abstand der zu brennbaren Materialien eingehalten werden muss auf ein Minimum.</p>

  <h3>Schornsteinverlängerung und Kaminverlängerung günstig selbst aufbauen.</h3>
  <p>Aufgrund neuerer Verordnungen reicht die Höhe vieler bestehender Schornsteine nicht mehr aus. Durch bauliche Veränderungen der Umgebung oder auch vieler weiterer Gründe kann es dazu kommen, dass eine Schornsteinverlängerung nötig wird. In unserem Online Shop finden Sie Schornsteinverlängerungen in den Ausführungen doppelwandig oder einwandig. Jede Kaminverlängerung wird von Hand hergestellt und kann exakt nach Maß konfiguriert werden. Hier kaufen Sie eine <span class="hl">Schornsteinverlängerung</span> für die Ewigkeit.</p>

  <h3>Leichtbauschornstein F90 und eine Wanddurchführung: Brandschutz auf höchstem Niveau.</h3>
  <p>Ein Edelstahlschornstein eignet sich hervorragend als nachträglicher Abgasleitung neben einem bereits gemauerten Schornstein im Gebäude. Was aber, wenn Ihnen die Optik nicht zusagt oder Sie lieber den Schornstein im Inneren unsichtbar verschwinden lassen möchten? Dafür ist der <span class="hl">Leichtbauschornstein</span> von Feronis prädestiniert. In Verbindung mit einer feuerfesten <span class="hl">Wanddurchführung</span> haben Sie hier das perfekte Duo für einen sicheren Zusatzschornstein.</p>

  <h3>Schornsteinabdeckung, Kaminabdeckung und Kaminabdeckplatte aus Edelstahl nach Maß.</h3>
  <p>Ältere Schornsteinköpfe unterliegen starken Belastungen durch Witterungseinflüsse. Nach vielen Jahren des Regens, Sonnenscheins, der Kälte und der Wärme werden Schornsteinköpfe porös und beginnen zu bröckeln. Dann wird es höchste Zeit für eine Kaminabdeckplatte und eine <span class="hl">Schornsteinabdeckung</span>. Bei Kaminabdeckungen gibt es die bekannte Napoleonhaube und Modinger Scheibe. Diese Modelle haben sich über viele Jahre bewährt und sind auf den meisten Gebäuden auch montiert. Bei brunnfeld-bauwaren finden Sie maßangefertigte Schornsteinabdeckungen aus Edelstahl oder Kupfer mit 25 Jahren Garantie.</p>

  <h3>Rauchsauger, Zugbegrenzer, Kamintüren und andere Spezialprodukte</h3>
  <p>Im Sortiment dieses Onlineshops finden Sie auch noch viele weitere Produkte rund um das Thema Schornstein und Abgastechnik. Hier wäre beispielsweise der <span class="hl">Rauchsauger</span> zu nennen. Ein sehr wichtiges Gerät, mit dem Sie den Schornsteinzug elektrisch verstärken können. Ebenfalls aus der Kategorie der Zugregelung und Zugverbesserung gibt es den Zugbegrenzer. Diese sogenannten Nebenluftvorrichtungen regeln rein mechanisch den Schornsteinzug. In manchen Fällen kann auch eine Abgasklappe notwendig werden. Neben der thermischen Abgasklappe finden Sie hier auch motorische Abgasklappen, die für Kaskaden oder Schornsteine mit Doppelbelegung notwendig sein können. Zu guter Letzt ist noch die Kamintüre zu erwähnen. Dieses Bauteil haben die meisten von Ihnen in der Schornsteinwange verbaut. Hier finden Sie passenden Ersatz, sollte es mal durchgerostet sein.</p>
  <p style="margin-top:26px">Viel Spaß beim Einkaufen, wünscht Ihnen das Team von brunnfeld-bauwaren.</p>
</div></section>

<section class="trust">
  <h2>Sicher einkaufen</h2>
  <div class="wrap">
    <div class="trust-box"><span class="flag" role="img" aria-label="Siegel: hergestellt in Deutschland"></span><p>Wir bieten ausschließlich Waren von deutschen Markenherstellern an. Unser gesamtes Sortiment wird von Branchenführern hergestellt und unterliegt ständigen Qualitätskontrollen. Für Ihre Sicherheit nur das Beste zum fairen Preis.</p></div>
    <div class="trust-box"><span class="seal" role="img" aria-label="Siegel: 25 Jahre Garantie"></span><p>Um unserem Premiumanspruch und unseren Leistungsversprechen gerecht zu werden, erhalten Sie bei uns selbstverständlich auch 25 Jahre Garantie auf alle Edelstahlschornsteine und Edelstahlschornstein Bauteile.</p></div>
  </div>
</section>

<footer class="footer"><div class="wrap">
  <div>Häufige Fragen<br>AGB<br>Lieferung &amp; Zahlung<br>Impressum<br>Blog</div>
  <div>Über uns<br>Widerruf<br>Datenschutz<br>Kontaktieren Sie uns<br>Glossar</div>
  <div>© 2011 - 2016 Kessler Bau GmbH<br>Lindenweg 14<br>86150 Augsburg<br>Germany</div>
  <div>Flue-Partners<br>Average rating<br>4.71 (of 5). Calculated from 265 reviews.</div>
  <div><strong>Kostenlose Beratung</strong><br><span class="tel">0821 / 447 318 0</span><br>Mo. – Fr. von 09:00 bis 18:00 Uhr<br>info@brunnfeld-bauwaren.de</div>
</div></footer>

<section class="pay"><div class="wrap">
  <span class="label">Zahlungsarten</span>
  <span class="card-mark">Kartana</span>
  <span class="card-mark">Zahlfix</span>
  <span class="card-mark">Netpay</span>
  <span class="card-mark">Direktly</span>
  <span class="card-mark">Vorkasse</span>
  <span class="card-mark">Globcard</span>
  <span class="card-mark">Bankra</span>
  <div class="social"><i></i><i></i><i></i><i></i><i></i></div>
</div></section>

</body>
</html>
```